Commercial LED Lighting Company need Product Catalog

We need a product catalog for our commercial LED Lighting company. We sell indoor and outdoor lighting fixtures to commercial customers, for commercial purposes. Most of our clients are knowledgeable about our products, and are interested in the technical details of our products.

Our catalog will offer 17 products, with a two page layout for each product. We have a specific vision for the general outline of the product layout. Attached, you will see a competitor's design whose layout we'd like to mimic - the first page for a product will have a large photo up top of a room or space showcasing the product, and the bottom half will be a photo of the product with some general bullet points. The second page will list the various model numbers for the products, along with their technical details. All information needed for the project will be provided, including product photos. We will not include all product photos in our attachment today, as we are limited to how many files we can upload at this time. Also attached is a general outline of the catalog, as well as product details.

Our clients are professionals, and we want to communicate a respect for our clients' know how and industry experience. We also want to maintain our color palate of blue, white and grey. I will also attach our logo to give you a reference.

Sample designs should include a potential cover design, and a two page layout for a single product.

Target Market(s)

LED Lighting Distributors; engineers; professional customers

Industry/Entity Type

Manufacturer

Font styles to use
Sans Serif

Colors
0355a3
cfdeed
85acd3
3276b5
eaf1f7

Requirements
Must have
• All required technical information as outlined in attached documents; all 17 products; the two page layout we have envisioned; our color scheme.

```html
<!DOCTYPE html>
<html lang="en">
<head>
<meta charset="utf-8">
<title>Corvel Lighting – LED Panel Catalog Spread</title>
<link href="https://fonts.googleapis.com/css2?family=Ubuntu:wght@300;400;500;700&family=Open+Sans:wght@400;600&display=swap" rel="stylesheet">
<style>
:root{
  --blue-deep:#0355a3;
  --blue-mid:#3276b5;
  --blue-soft:#85acd3;
  --blue-pale:#cfdeed;
  --blue-mist:#eaf1f7;
  --ink:#3a3d42;
  --grey-text:#6b6f75;
  --grey-bar:#3b3d40;
  --page:#ffffff;
  --backdrop:#d9dadb;
}
*{box-sizing:border-box;margin:0;padding:0}
html,body{width:1200px;height:804px;overflow:hidden;background:var(--backdrop);font-family:"Open Sans",sans-serif;color:var(--ink)}
.spread{position:absolute;left:60px;top:20px;width:1080px;height:764px;display:flex;box-shadow:0 6px 24px rgba(0,0,0,.18)}
.page{position:relative;width:540px;height:764px;background:var(--page);overflow:hidden}
.page--left{border-right:1px solid #e3e5e8}

/* left page */
.hero-photo{position:absolute;left:0;top:0;width:540px;height:420px;background:linear-gradient(160deg,#e9edf1 0%,#c9d1d9 45%,#8b939c 80%,#5f656c 100%)}
.title-band{position:absolute;left:0;top:286px;width:540px;height:58px;background:linear-gradient(90deg,var(--blue-deep) 0%,var(--blue-mid) 55%,rgba(50,118,181,.35) 100%);display:flex;align-items:center;padding-left:58px}
.title-band h1{font-family:"Ubuntu",sans-serif;font-weight:500;font-size:36px;color:#fff}
.intro{position:absolute;left:30px;top:444px;width:250px;font-size:9.4px;line-height:1.45;color:var(--ink)}
.product-shot{position:absolute;left:290px;top:436px;width:220px;height:150px;border-radius:10px;background:radial-gradient(ellipse at 50% 55%,#ffffff 0%,#e8eaed 60%,#cfd3d8 100%)}
.badges{position:absolute;display:flex;gap:8px}
.badge{width:22px;height:22px;border-radius:50%;background:#4a4d52}
.badge--light{background:#fff;border:2px solid #4a4d52}
.page--left .badges{left:450px;top:598px}
.section-head{font-family:"Ubuntu",sans-serif;font-weight:500;color:var(--blue-mid);font-size:14px}
.bullets{list-style:none;margin-top:6px}
.bullets li{font-size:9.4px;line-height:1.55;padding-left:13px;position:relative}
.bullets li::before{content:"";position:absolute;left:0;top:4px;width:7px;height:7px;background:var(--blue-mid)}
.benefits{position:absolute;left:36px;top:580px;width:460px}
.areas{position:absolute;left:36px;top:648px;width:460px}
.footer{position:absolute;bottom:0;left:0;width:540px;height:44px;display:flex}
.footer .web{width:170px;background:linear-gradient(90deg,var(--blue-deep),var(--blue-mid));color:#fff;font-size:10px;display:flex;align-items:center;justify-content:center}
.footer .contact{flex:1;background:var(--grey-bar);color:#fff;font-size:10px;display:flex;align-items:center;justify-content:center;position:relative}
.page-num{position:absolute;top:8px;width:26px;height:26px;border-radius:50%;background:#fff;border:3px solid var(--blue-mid);color:var(--blue-deep);font-size:11px;font-weight:600;display:flex;align-items:center;justify-content:center}
.page--left .page-num{right:14px}
.page--right .page-num{left:14px}

/* right page */
.running-head{position:absolute;left:40px;top:40px;font-family:"Ubuntu",sans-serif;font-size:8px;letter-spacing:1px;color:var(--ink);line-height:1.3}
.head-rule{position:absolute;left:40px;top:58px;width:370px;height:1px;background:var(--ink)}
.brand{position:absolute;right:34px;top:40px;display:flex;align-items:center;gap:6px}
.brand .mark{width:9px;height:9px;background:var(--blue-mid)}
.brand span{font-family:"Ubuntu",sans-serif;font-weight:500;font-size:12px;color:var(--blue-deep);line-height:1}
.fixture{position:absolute;left:40px;width:470px}
.fixture--a{top:80px}
.fixture--b{top:390px}
.fixture h2{font-family:"Ubuntu",sans-serif;font-weight:300;font-size:21px;color:var(--grey-text)}
.fixture .section-head{margin-top:12px}
.fixture .bullets{width:265px}
.fixture .bullets li{font-size:8.4px;line-height:1.55}
.tech{margin-top:12px}
.tech-table{border-collapse:collapse;margin-top:4px;width:210px;font-size:8.2px}
.tech-table td{border:1px solid var(--blue-pale);padding:1px 6px;text-align:center;height:12px}
.tech-table tr:nth-child(odd) td{background:var(--blue-mist)}
.tech-table td:first-child{width:104px}
.frame{position:absolute;right:0;top:20px;width:190px;height:200px;border:1.5px solid var(--blue-soft);border-radius:12px}
.frame .shot{position:absolute;left:15px;top:26px;width:160px;height:120px;border-radius:6px;background:radial-gradient(ellipse at 50% 60%,#f6f7f8 0%,#dde1e5 70%,#f4f5f6 100%)}
.frame .badges{left:110px;top:160px}
</style>
</head>
<body>
<main class="spread">
  <section class="page page--left">
    <div class="hero-photo" role="img" aria-label="Bright office interior lit by recessed LED flat panels, with bookshelves and windows"></div>
    <div class="title-band"><h1>Led Panel</h1></div>
    <p class="intro">Led Flat Panel provides lighting customers with quality LED flat panel solutions for use in recessed and suspended commercial applications, all backed by the industry leader in LED lighting technology - Corvel Lighting. The fully luminous flat panel with an optically-efficient, edge-lit design transforms any space with soft, low-glare illumination while providing exceptional application flexibility, performance, and return on investment.</p>
    <div class="product-shot" role="img" aria-label="Square white LED flat panel fixture"></div>
    <div class="badges"><span class="badge badge--light"></span><span class="badge"></span></div>
    <div class="benefits">
      <h3 class="section-head">Product Benefits:</h3>
      <ul class="bullets">
        <li>Quick and simple installation</li>
        <li>Attractive and functional design</li>
        <li>Opal cover above LEDs for homogeneous illumination and minimized glare</li>
      </ul>
    </div>
    <div class="areas">
      <h3 class="section-head">Areas of Application:</h3>
      <ul class="bullets">
        <li>Foyers</li>
        <li>Conference rooms</li>
        <li>Corridors, entrances, foyers, stairwells, elevators</li>
      </ul>
    </div>
    <footer class="footer">
      <div class="web">www.corvellighting.com</div>
      <div class="contact">555-014-2290 | info@corvellighting.com<span class="page-num">2</span></div>
    </footer>
  </section>

  <section class="page page--right">
    <div class="running-head">CORVEL LIGHTING<br>YOUR CREATIVE COMMERCIAL STYLE</div>
    <div class="head-rule"></div>
    <div class="brand"><span class="mark"></span><span>Corvel Lighting</span></div>

    <article class="fixture fixture--a">
      <h2>Led Flat Panel Fixture 2 X2</h2>
      <h3 class="section-head">Features and Benefits</h3>
      <ul class="bullets">
        <li>Widely used for indoor commercial general lighting purpose</li>
        <li>Replace 2x2 recessed or surface mount florescent fixtures</li>
        <li>Design to provide an even and smooth lighting distribution to the floor</li>
        <li>Safety listed and efficiency qualified</li>
        <li>6 years warranty</li>
      </ul>
      <div class="tech">
        <h3 class="section-head">Technical Data</h3>
        <table class="tech-table">
          <tr><td>Beam Angle</td><td>180 Degrees</td></tr>
          <tr><td>CRI</td><td>&gt; 80</td></tr>
          <tr><td>Operation Temperature</td><td>-30°C to 60°C</td></tr>
          <tr><td>Lifespan</td><td>50,000 Hours</td></tr>
          <tr><td>Waterproof Rating</td><td>Damp Location</td></tr>
          <tr><td>Dimming</td><td>0-10 V</td></tr>
        </table>
      </div>
      <div class="frame">
        <div class="shot" role="img" aria-label="Suspended 2x2 LED flat panel fixture"></div>
        <div class="badges"><span class="badge badge--light"></span><span class="badge"></span></div>
      </div>
    </article>

    <article class="fixture fixture--b">
      <h2>Led Flat Panel Fixture 2 X4</h2>
      <h3 class="section-head">Features and Benefits</h3>
      <ul class="bullets">
        <li>Widely used for indoor commercial general lighting purpose</li>
        <li>Replace 2x4 recessed or surface mount florescent fixtures</li>
        <li>Design to provide an even and smooth lighting distribution to the floor</li>
        <li>Safety listed and premium efficiency qualified</li>
        <li>6 years warranty</li>
      </ul>
      <div class="tech">
        <h3 class="section-head">Technical Data</h3>
        <table class="tech-table">
          <tr><td>Beam Angle</td><td>180 Degrees</td></tr>
          <tr><td>CRI</td><td>&gt; 80</td></tr>
          <tr><td>Operation Temperature</td><td>-30°C to 60°C</td></tr>
          <tr><td>Lifespan</td><td>50,000 Hours</td></tr>
          <tr><td>Waterproof Rating</td><td>Damp Location</td></tr>
          <tr><td>Dimming</td><td>0-10 V</td></tr>
          <tr><td>Lumen per watt</td><td>130 lm/w</td></tr>
        </table>
      </div>
      <div class="frame">
        <div class="shot" role="img" aria-label="Rectangular 2x4 LED flat panel fixture"></div>
        <div class="badges"><span class="badge badge--light"></span><span class="badge"></span></div>
      </div>
    </article>

    <footer class="footer">
      <div class="contact"><span class="page-num">3</span>555-014-2290 | info@corvellighting.com</div>
      <div class="web">www.corvellighting.com</div>
    </footer>
  </section>
</main>
</body>
</html>
```